Valentine's Day menu

Our establishment on 17, (bar - brasserie - wine bar); Offers a menu for Valentine's Day, one that will be on site and another in delivery.

Menu on site:

Starter: Oysters, warm champagne flambé

Dish: Grilled tournedos, braised endives and Jerusalem artichokes
Ranger Sauce
Sole meunière, lemon sauce, steamed potatoes, rice

Dessert: Tiramisu with red fruits - Flambéed Crêpe Suzette

Menu at 29.90€

Delivery menu: Raclette platter with Savoy cheeses - Pierrade platter and fresh vegetables.
Half-bottle of VERMELLE BLANCS DE BLANS.

Please use the Valentine's Day theme, use our logo and colors (attached). The goal is to get as many reservations as possible.

Reservation required at: 06 52 87 30 19
17
11 rue Honorine Vastel 59730 SORVAL

I remain at your disposal.

- Rate ; 45€ / Person

```html
<!DOCTYPE html>
<html lang="fr">
<head>
<meta charset="utf-8">
<title>Le Dix-Sept – Menu Saint-Valentin</title>
<link href="https://fonts.googleapis.com/css2?family=Arimo:wght@400;700&family=Kaushan+Script&display=swap" rel="stylesheet">
<style>
  :root{
    --backdrop:#ffffff;
    --paper:#ffffff;
    --ink:#1a1a1a;
    --gold:#c98a16;
    --gold-light:#f2c548;
    --gold-dark:#a9700c;
    --pink-frame:#f6bfd4;
    --pink-soft:#fbdbe7;
    --pink-hot:#e2195b;
    --crimson:#b4103f;
  }
  *{box-sizing:border-box;margin:0;padding:0}
  html,body{width:1200px;height:1000px;overflow:hidden;background:var(--backdrop)}
  .flyer{
    position:absolute;left:294px;top:65px;width:616px;height:873px;
    background:linear-gradient(to bottom,var(--paper) 0%,var(--paper) 72%,#fde6ee 88%,#fbd6e3 100%);
    font-family:"Arimo",Arial,sans-serif;color:var(--ink);overflow:hidden;
  }
  .frame{position:absolute;inset:0;pointer-events:none}
  .hearts{position:absolute}
  .hearts--tl{left:0;top:0;width:110px;height:120px;background:radial-gradient(circle at 40% 45%,var(--pink-hot) 0%,#f07aa0 45%,rgba(251,219,231,0) 72%)}
  .hearts--tr{right:0;top:0;width:150px;height:130px;background:radial-gradient(circle at 65% 45%,var(--pink-hot) 0%,#f59cbb 45%,rgba(251,219,231,0) 72%)}
  .hearts--bl{left:0;bottom:0;width:170px;height:150px;background:radial-gradient(circle at 35% 75%,var(--crimson) 0%,var(--pink-hot) 35%,#f5a4c0 55%,rgba(251,219,231,0) 75%)}
  .hearts--br{right:0;bottom:0;width:150px;height:140px;background:radial-gradient(circle at 65% 75%,var(--crimson) 0%,var(--pink-hot) 35%,#f5a4c0 55%,rgba(251,219,231,0) 75%)}

  .brand{position:absolute;top:34px;left:0;width:100%;text-align:center}
  .brand__name{display:inline-flex;align-items:center;gap:12px;font-size:28px;font-weight:400;letter-spacing:3px;color:var(--gold)}
  .brand__dot{width:30px;height:30px;border-radius:50%;border:2px solid var(--gold)}
  .brand__tagline{display:flex;justify-content:center;gap:70px;font-size:6px;letter-spacing:.6px;margin-top:3px}

  .title{position:absolute;left:0;width:100%;text-align:center;font-family:"Kaushan Script",cursive;line-height:1;font-weight:400}
  .title--line1{top:98px;font-size:44px;color:var(--ink)}
  .title--line2{top:148px;font-size:56px;color:var(--gold-light);text-shadow:2px 3px 0 var(--gold-dark),3px 5px 4px rgba(0,0,0,.25)}

  .block{position:absolute;left:0;width:100%;text-align:center;font-weight:700;font-size:14.5px;line-height:17px}
  .ribbon{position:absolute;left:50%;transform:translateX(-50%);height:30px;display:flex;align-items:center;justify-content:center}
  .ribbon svg{position:absolute;inset:0;width:100%;height:100%}
  .ribbon span{position:relative;color:#fff;font-weight:700;font-size:18px}
  .divider{position:absolute;left:50%;width:116px;margin-left:-58px;height:2px;background:var(--gold)}
  .price{color:var(--gold);font-size:23px;line-height:27px}
  .price--single{font-size:24px}
  .small{font-size:14px}
  .phone{color:var(--gold)}
  .rate{position:absolute;left:161px;top:816px;width:292px;height:31px;border-radius:6px;
    background:linear-gradient(to bottom,var(--gold-light),var(--gold));
    color:#fff;font-weight:700;font-size:22.5px;display:flex;align-items:center;justify-content:center}
</style>
</head>
<body>
<main class="flyer">
  <svg class="frame" width="616" height="873" viewBox="0 0 616 873">
    <rect x="22" y="90" width="7" height="660" fill="var(--pink-frame)"/>
    <rect x="34" y="90" width="2" height="660" fill="var(--pink-soft)"/>
    <rect x="587" y="90" width="7" height="660" fill="var(--pink-frame)"/>
    <rect x="580" y="90" width="2" height="660" fill="var(--pink-soft)"/>
    <line x1="60" y1="55" x2="556" y2="55" stroke="var(--pink-soft)" stroke-width="2"/>
  </svg>

  <div class="hearts hearts--tl" role="img" aria-label="Cluster of paper-cut pink hearts"></div>
  <div class="hearts hearts--tr" role="img" aria-label="Cluster of paper-cut pink hearts"></div>
  <div class="hearts hearts--bl" role="img" aria-label="Cluster of paper-cut red and pink hearts"></div>
  <div class="hearts hearts--br" role="img" aria-label="Cluster of paper-cut red and pink hearts"></div>

  <header class="brand">
    <div class="brand__name"><span>LE DIX-SEPT</span><span class="brand__dot"></span></div>
    <div class="brand__tagline"><span>BAR BRASSERIE</span><span>COCKTAILS · BIÈRE · CHAMPAGNE · VINS</span></div>
  </header>

  <h1 class="title title--line1">Oysters, warm</h1>
  <h2 class="title title--line2">Champagne flambé</h2>

  <div class="ribbon" style="top:247px;width:150px">
    <svg viewBox="0 0 150 30" preserveAspectRatio="none"><polygon points="0,8 18,8 18,0 132,0 132,8 150,8 140,19 150,30 0,30 10,19" fill="var(--gold)"/><rect x="18" y="0" width="114" height="30" fill="var(--gold-light)"/></svg>
    <span>Dish:</span>
  </div>
  <div class="block" style="top:292px">Gegrilde tournedos, gesmoorde andijvie en aardpeer<br>Ranger Saus Sole meunière, citroensaus, gestoomde aardappelen, rijst</div>
  <div class="divider" style="top:340px"></div>
  <div class="block" style="top:355px">Plateau raclette aux fromages de Savoie<br>Plateau pierrade et légume frais</div>
  <div class="block price" style="top:391px">Le menu sur place est à 34.90€, +<br>un supplément de 10€ pour la saule.</div>
  <div class="block small" style="top:446px">Dans le menu à emporter, c'est du champagne VERLAINE.</div>

  <div class="ribbon" style="top:476px;width:150px">
    <svg viewBox="0 0 150 30" preserveAspectRatio="none"><polygon points="0,8 18,8 18,0 132,0 132,8 150,8 140,19 150,30 0,30 10,19" fill="var(--gold)"/><rect x="18" y="0" width="114" height="30" fill="var(--gold-light)"/></svg>
    <span>Nagerecht:</span>
  </div>
  <div class="block" style="top:518px">Tiramisu aux fruits rouges - Geflambeerde Crêpe Suzette</div>
  <div class="block price price--single" style="top:536px">Menu at 29.90€</div>

  <div class="ribbon" style="top:584px;width:208px">
    <svg viewBox="0 0 208 30" preserveAspectRatio="none"><polygon points="0,8 18,8 18,0 190,0 190,8 208,8 198,19 208,30 0,30 10,19" fill="var(--gold)"/><rect x="18" y="0" width="172" height="30" fill="var(--gold-light)"/></svg>
    <span>Delivery menu:</span>
  </div>
  <div class="block" style="top:631px">Racletteschotel met savooie kazen - Pierradeschotel<br>en vers groenten.<br>Couper en deux les fles VERMELLE BLANCS DE BLANS.</div>
  <div class="divider" style="top:690px"></div>
  <div class="block" style="top:699px">Merci d'indiquer une animation chanteur et guitariste.<br>Réservation souhaitée.</div>
  <div class="divider" style="top:740px"></div>
  <div class="block" style="top:757px">Réservation obligatoire au : <span class="phone">06 52 87 30 19</span><br>11 rue Honorine Vastel 59730 SORVAL<br>Je reste à votre disposition.</div>

  <div class="rate">- Taux ; 45€ / Personne</div>
</main>
</body>
</html>
```